Mortgage Broking boutique Business

I’m wanting a revamped look to my existing business card design. I do like the black and silver but happy to have other colours introduced based on your creation. I’ve attached a copy of my current card so you can have a starting point updated details noted brloe. I deal with high net worth individuals so need my card to be sophisticated, classy that gives off a classy vibe

Target Market(s)

High net worth, wealthy

Industry/Entity Type

Mortgage Brokerage

Contact Information for Business Card

Job title: Finance Executive
Phone: +61 7 3287 4419
Mobile: 0471 352 608
Email: marcus@quillbrookcapital.com.au
Web: www.quillbrookcapital.com.au
Address: level 36 Tindale Court, 58 Harwick St Brisbane QLD 4000

Font styles to use
Other font styles liked:
• Helvetica

Colors

Designer to choose colors to be used in the design.

Requirements
Must have
• Use my existing card design as a starting point

```html
<!DOCTYPE html>
<html lang="en">
<head>
<meta charset="utf-8">
<title>Quillbrook Capital — Business Card</title>
<link rel="stylesheet" href="https://fonts.googleapis.com/css2?family=Inter:wght@400;500&family=Lato:wght@300;400&display=swap">
<style>
  :root {
    --page: #ffffff;
    --card: #000000;
    --silver: #b9bbbd;
    --silver-dim: #9a9a9a;
    --silver-faint: #8a8a8a;
    --white: #ffffff;
    --rule-mid: #c9c9c9;
  }
  * { margin: 0; padding: 0; box-sizing: border-box; }
  html, body {
    width: 1200px; height: 1200px; overflow: hidden;
    background: var(--page);
  }
  .sheet { position: relative; width: 1200px; height: 1200px; }

  .card {
    position: absolute;
    width: 772px; height: 441px;
    background: var(--card);
    overflow: hidden;
  }
  .card--front { left: 218px; top: 106px; }
  .card--back  { left: 224px; top: 659px; }

  .brand {
    position: absolute;
    display: flex; flex-direction: column; align-items: center;
    font-family: "Inter", Helvetica, Arial, sans-serif;
    font-weight: 400;
    color: var(--white);
    text-transform: uppercase;
    line-height: 1;
  }
  .brand__name { font-size: 21px; letter-spacing: 5px; }
  .brand__sub  { font-size: 12px; letter-spacing: 4px; margin-top: 9px; }
  .card--front .brand { left: 0; width: 772px; top: 182px; }
  .card--back .brand  { left: 478px; width: 240px; top: 170px; }

  .rule {
    position: absolute; left: 28px; width: 717px; height: 1px;
    top: 355px;
    background: linear-gradient(90deg, rgba(201,201,201,0) 0%, var(--rule-mid) 30%, var(--rule-mid) 70%, rgba(201,201,201,0) 100%);
  }

  .web-front {
    position: absolute; left: 0; width: 772px; top: 357px;
    text-align: center;
    font-family: "Lato", Helvetica, Arial, sans-serif;
    font-weight: 300; font-size: 19px; letter-spacing: 3.4px;
    color: var(--silver-dim);
  }

  .person { position: absolute; left: 97px; top: 82px; }
  .person__name {
    font-family: "Inter", Helvetica, Arial, sans-serif;
    font-weight: 400; font-size: 41px; letter-spacing: -1px;
    color: var(--silver); line-height: 1;
  }
  .person__title {
    margin-top: 11px;
    font-family: "Inter", Helvetica, Arial, sans-serif;
    font-size: 10.5px; letter-spacing: 2.6px;
    color: #d8d8d8;
  }
  .person__underline {
    width: 31px; height: 1px; background: #d8d8d8; margin-top: 4px;
  }

  .contact {
    position: absolute; left: 97px; top: 185px;
    list-style: none;
    font-family: "Lato", Helvetica, Arial, sans-serif;
    font-weight: 300; font-size: 17px; letter-spacing: 2.4px;
    color: var(--silver-dim);
  }
  .contact li { height: 29.6px; line-height: 22px; }

  .address {
    position: absolute; left: 0; width: 772px; top: 375px;
    text-align: center;
    font-family: "Lato", Helvetica, Arial, sans-serif;
    font-weight: 300; font-size: 14.5px; letter-spacing: 3.6px;
    color: var(--silver-faint);
  }
</style>
</head>
<body>
  <main class="sheet">
    <section class="card card--front" aria-label="Card front">
      <div class="brand">
        <span class="brand__name">Quillbrook</span>
        <span class="brand__sub">Capital</span>
      </div>
      <div class="rule"></div>
      <p class="web-front">www.quillbrookcapital.com.au</p>
    </section>

    <section class="card card--back" aria-label="Card back">
      <div class="person">
        <h1 class="person__name">MARCUS HALE</h1>
        <p class="person__title">Finance Executive</p>
        <div class="person__underline"></div>
      </div>
      <ul class="contact">
        <li>+61 7 3287 4419</li>
        <li>0471 352 608</li>
        <li>marcus@quillbrookcapital.com.au</li>
        <li>www.quillbrookcapital.com.au</li>
      </ul>
      <div class="brand">
        <span class="brand__name">Quillbrook</span>
        <span class="brand__sub">Capital</span>
      </div>
      <div class="rule"></div>
      <p class="address">level 36 Tindale Court, 58 Harwick St Brisbane QLD 4000</p>
    </section>
  </main>
</body>
</html>
```